Tervolan Pty Ltd professional business card

A professional business card template using the colours from the supplied logo.
Clean crisp lines while, Modern while not being over the top.

Target Market(s)

Construction, commerical and industrial

Industry/Entity Type

Communications

Contact Information for Business Card

For a Communications, IT, Optical fibre installation company

Colors
37b8a4

```html
<!DOCTYPE html>
<html lang="en">
<head>
<meta charset="utf-8">
<title>Tervolan Pty Ltd – Business Card</title>
<link href="https://fonts.googleapis.com/css2?family=Montserrat:wght@400;500;700&display=swap" rel="stylesheet">
<style>
  :root {
    --backdrop: #1d1d1d;
    --card-light: #f6f5f3;
    --card-dark: #2a2a2a;
    --teal: #1c8f9b;
    --grey: #6d6e71;
    --ink: #2b2b2b;
    --white: #ececec;
  }
  * { margin: 0; padding: 0; box-sizing: border-box; }
  html, body {
    width: 1200px; height: 782px; overflow: hidden;
    background: var(--backdrop);
    font-family: "Montserrat", Arial, sans-serif;
  }
  .canvas { position: relative; width: 1200px; height: 782px; }

  .card {
    position: absolute; top: 241px;
    width: 522px; height: 299px;
    border-radius: 14px; overflow: hidden;
  }
  .card--front { left: 74px; background: var(--card-light); }
  .card--back { left: 605px; background: var(--card-dark); }

  .wordmark {
    position: absolute; display: flex; align-items: center; gap: 10px;
    font-weight: 500; line-height: 1; letter-spacing: 0.5px;
  }
  .wordmark__dot { border-radius: 50%; background: var(--teal); flex: none; }
  .card--front .wordmark { left: 20px; top: 28px; font-size: 40px; color: var(--grey); }
  .card--front .wordmark__dot { width: 26px; height: 26px; }
  .card--back .wordmark { left: 0; right: 0; top: 140px; justify-content: center; font-size: 52px; color: var(--white); }
  .card--back .wordmark__dot { width: 32px; height: 32px; }

  .tab {
    position: absolute; left: 0; top: 128px;
    width: 11px; height: 39px; background: var(--teal);
    border-radius: 0 4px 4px 0;
  }
  .person { position: absolute; left: 23px; top: 128px; }
  .person__name { font-size: 19.5px; font-weight: 700; color: var(--teal); letter-spacing: 0.4px; line-height: 1.1; }
  .person__role { font-size: 13.5px; font-weight: 400; color: var(--ink); margin-top: 6px; }
  .rule { position: absolute; left: 23px; top: 192px; width: 26px; height: 2px; background: var(--teal); }

  .contact-block {
    position: absolute; left: 23px; top: 220px;
    display: flex; align-items: flex-end; gap: 12px;
  }
  .contacts { list-style: none; }
  .contacts li {
    display: flex; align-items: center; gap: 7px;
    font-size: 13.5px; color: var(--ink); height: 21px; line-height: 21px;
    white-space: nowrap;
  }
  .contacts svg { width: 12px; height: 13px; flex: none; fill: var(--teal); }
  .divider { width: 2px; height: 36px; margin-bottom: 3px; background: var(--teal); flex: none; }
  .address {
    font-style: normal; font-size: 13.5px; color: var(--ink);
    line-height: 21px; white-space: nowrap;
  }

  .site {
    position: absolute; left: 0; right: 0; top: 263px;
    text-align: center; font-size: 14.5px; letter-spacing: 1.2px; color: var(--white);
  }
</style>
</head>
<body>
<main class="canvas">
  <section class="card card--front">
    <div class="wordmark"><span class="wordmark__dot"></span>TERVOLAN</div>
    <span class="tab"></span>
    <div class="person">
      <p class="person__name">DANIEL ROWCROFT</p>
      <p class="person__role">Managing Director</p>
    </div>
    <span class="rule"></span>
    <div class="contact-block">
      <ul class="contacts">
        <li><svg viewBox="0 0 12 14"><path d="M3 0h6a1.5 1.5 0 0 1 1.5 1.5v11A1.5 1.5 0 0 1 9 14H3a1.5 1.5 0 0 1-1.5-1.5v-11A1.5 1.5 0 0 1 3 0zm0 1.5v9.5h6V1.5zm3 10.3a.8.8 0 1 0 0 1.6.8.8 0 0 0 0-1.6z"/></svg>+61 400 318 264</li>
        <li><svg viewBox="0 0 12 14"><path d="M0 3.5h12v7H0zm1 .8L6 8l5-3.7V4H1z"/></svg>daniel.r@tervolan.com</li>
        <li><svg viewBox="0 0 12 14"><circle cx="6" cy="7" r="5.5"/><path d="M3 5.5c1-.8 2 .3 2.5 1s-.5 2 .5 2.5-.3 2-1 2.2M8.5 3.5c-.5 1 .5 1.5 1.3 1.8" stroke="#f6f5f3" stroke-width="1" fill="none"/></svg>www.tervolan.com</li>
      </ul>
      <span class="divider"></span>
      <address class="address">4120 Harbour Lane<br>Portland, OR 97205</address>
    </div>
  </section>

  <section class="card card--back">
    <div class="wordmark"><span class="wordmark__dot"></span>TERVOLAN</div>
    <p class="site">www.tervolan.com</p>
  </section>
</main>
</body>
</html>
```